Creating business cards for our new private medical clinic in London

Hey everyone,

We are starting a new private medical clinic in central London. We already have our logo (please see the 2 different layouts of the logo attached.) Please note that we are not restricted to using only this font in the card though.

The cards will be printed by "Pekko." The cards have a textured surface and a coloured middle layer - please see this webpage for the exact product spec (https://www.pekkoprint.example/uk/products/velvet/business-cards.html). We're overall looking for a modern yet highly professional look. We'd like the cards to have Square edges and NOT rounded please.

We need a standard card that uses one or both of our logo's colours (blue and green), and another card for premium customers, that uses black with either gold/silver/bronze. On the black coloured cads, please could you add the word "Black Account" or the word "Black" under the logo text - wherever you think it looks best?

_________________

AMENDMENT TO BRIEF:

1) The first batch of our cards are to be promotional cards and need to have more information. Could please have one card that is more like an "information card" that has the following information: - (There's a lot there and we might need to slim this down once we see the cards.)

GP appointments £70
-Feeling unwell
-Referrals to private specialists
-Sexual health check up
-Contraception
-Second opinion

Launch Offer
First appointment £40 with this card until 30 September 2017

Book online

2) Could you see whether we could add a 'strap line' to the card, something like: “Stay in Optimal Health”

_____________

The files attached have 2 versions of our logo - one linear and with the words 'stacked'; we think that the stacked logo may work better for the business card but we'd love to see different versions.

On one side of the card could we please see a coloured background, with a design containing our logo? On the other side of the card, please could we have a different coloured or white background and the information below.

Address: THE HARROWFIELD CLINIC @ FitVanta, 19 Bramblecote Lane, London, EC2Z 4QJ
Open: Mon-Fri (early & late appointments)
Book Online: www.harrowfieldclinic.example
Email: bookings@harrowfieldclinic.example
Phone number: (We don't have this yet - but please leave a space for this to go into.)

Other possible design features:

Because our clinic is located in the financial district of London, anything that represents this (e.g. The City of London's skyline - i.e. financial district - could look nice (example buildings include: The Pinecone, The Teacup-Tower, The Wedgehouse, St Aldric Minster, Keep of Brennmoor, Gantry Crossing, The Spindle). We wondered whether a outline or drawing of these buildings in the background of the card could look nice. Please see the image link below to get an idea of the skyline we're looking for:

https://img.stockvale.example/z/skyline-hand-drawn-city-pastel-shades-heritage-buildings-futuristic-81920457.jpg

The following image links are examples of cards that we've seen online and like the overall feel of (of course our colours are different):

http://www.craftnook.example/diverse/2/goodcards/73014589122.jpg
http://cardheron.example/wp-content/uploads/2013/01/cool-business-cards-saffron.jpg
https://cardfolio.example/wp-content/uploads/20461-cool-business-card-mockup.jpg
http://www.plinthworks.example/wp-content/uploads/edd/2015/08/Modern-Tutor-Business-Card-Template-Preview.jpg
http://lorvelandkit.example/wp-content/uploads/2017/01/design-a-business-card-cool-business-card-designsqx83.jpg
http://makerspindle.example/resources/files/articles/harbor-print/copper-foil-business-cards.jpg

STATIONARY:
We will also need the following stationary designed by our chosen designer. We’d like stationary to use one or both the colours of our logo (ie Green and Blue). Please use these colours to add any additional design features to stationary - other similar palette colours can also be used. Our logo font is - abeatbyKai - and this could be used in other parts of the stationary, but please feel free to try other fonts too. We prefer sans serif fonts.

Overall - we are open to all ideas but we need a look and feel that looks modern and highly professional. For our letter, prescription and medical report templates we need these to be PDFs and word processing files that can merge relevant data and text into different sections.

The information required on various pieces of stationary are as follows:

Letterheads:
These need to have:
Clinic's: Logo / Address / Phone Number / Website / Email address / Recipients address.
The letter can have address data either at the top or as a footer. We're happy to see designs that use either to see which one looks best (same goes for other pieces of stationary too.)

Invoices:
Invoice number: (Unique code for document)
Invoice Date:
Clinic’s: Logo / Address / Phone Number / Website / Email address
Services: Service Code / Name of Service / Price
Total Price:
PAYLO, Cardwise and Northern Remit Logos
Patient details: Patient’s Name / Address

Prescription Pads:
Prescription number: (Unique code for document)
Clinic details: Clinic’s Logo / Address / Phone Number / Website / Email address
Patient details needed include: Patient’s Name / Date of birth / address
Blank space required to write the name of medication
Doctors Signature: and space for signature
MPB Number: and space for this to be entered

Templates for our medical reports:
These are reports we will be printed (on good quality paper) for patients after they have had a complete health check. They will include a text summary, and the results of any tests (with graphs) and images of scans. Please could we see how text/titles/headings/tables etc could be styled?
They will need the following details: -
Clinic details needed include: Clinic’s Logo / Address / Phone Number / Website / Email address
Date of Report:
Then the following sections need to be includes:
1) Free Text Space
2) Space for images and text
3) Space for blood test and text

___________________

Thanks so much everyone.

All the best,

Tev and Dane

Target Market(s)

City of London
Private Healthcare

Industry/Entity Type

Health Care

Contact Information for Business Card

Font styles to use
Sans Serif

Colors
33a6d7
25a0d3
add136
9bcb3c
cadf82
85acd3
3276b5
0255a3
85cae6

Requirements
Must have
• Please see project description for details.
Nice to have
• Perhaps a outline/drawing/illustration of the City of London skyline (i.e. the Pinecone and surrounding buildings)

```html
<!DOCTYPE html>
<html lang="en">
<head>
<meta charset="utf-8">
<title>The Harrowfield Clinic – Business Cards</title>
<link rel="stylesheet" href="https://fonts.googleapis.com/css2?family=Open+Sans:wght@300;400;600&display=swap">
<style>
  :root {
    --clinic-blue: #4aa9d4;
    --clinic-blue-pale: #bfe1f1;
    --clinic-green: #9bcb3c;
    --paper: #ffffff;
    --ink-grey: #555a5e;
    --backdrop: #e4e6e8;
  }
  * { box-sizing: border-box; margin: 0; padding: 0; }
  html, body {
    width: 1200px; height: 824px; overflow: hidden;
    background: var(--backdrop);
    font-family: "Open Sans", Arial, sans-serif;
  }
  .canvas { position: relative; width: 1200px; height: 824px; }

  .card {
    position: absolute;
    background: var(--paper);
    overflow: hidden;
    box-shadow: 0 2px 6px rgba(0,0,0,0.12);
  }

  /* Front card: portrait, content set along the long edge */
  .card--front { left: 90px; top: 134px; width: 360px; height: 556px; }
  .card__rotated {
    position: absolute;
    left: -98px; top: 98px;
    width: 556px; height: 360px;
    transform: rotate(-90deg);
  }
  .blue-panel {
    position: absolute; left: 0; top: 0;
    width: 320px; height: 360px;
    background: var(--clinic-blue);
  }
  .skyline {
    position: absolute; left: 300px; top: 0;
    width: 150px; height: 360px;
    background: linear-gradient(to right, var(--clinic-blue) 0%, var(--clinic-blue-pale) 65%, var(--paper) 100%);
  }

  .brand {
    position: absolute; top: 24px; right: 18px;
    display: flex; align-items: center; gap: 8px;
  }
  .brand__mark {
    width: 20px; height: 20px;
    background: var(--clinic-blue);
  }
  .brand__name {
    font-weight: 300; font-size: 21px;
    color: var(--clinic-blue);
    line-height: 1;
    letter-spacing: 0.2px;
  }
  .brand__tagline {
    position: absolute; top: 50px; right: 18px;
    font-size: 7px; letter-spacing: 1.2px;
    color: var(--ink-grey);
    text-transform: uppercase;
  }

  .contact {
    position: absolute; left: 150px; top: 132px;
    color: var(--paper);
    font-weight: 300;
  }
  .contact__name { font-size: 21px; letter-spacing: 0.6px; line-height: 1.1; }
  .contact__role { font-size: 14px; letter-spacing: 0.4px; margin-bottom: 12px; }
  .contact__address { font-size: 13px; line-height: 1.45; margin-bottom: 10px; }
  .contact__line {
    display: flex; align-items: center; gap: 7px;
    font-size: 13px; line-height: 1.5;
  }
  .contact__icon { width: 11px; height: 11px; flex: none; }

  /* Back card: landscape, white */
  .card--back { left: 510px; top: 231px; width: 600px; height: 388px; }
  .back-brand {
    position: absolute; left: 0; right: 0; top: 130px;
    display: flex; justify-content: center; align-items: center; gap: 10px;
  }
  .back-brand .brand__mark { width: 34px; height: 34px; }
  .back-brand .brand__name { font-size: 30px; }
  .opening-hours {
    position: absolute; left: 0; right: 0; top: 232px;
    text-align: center;
    font-size: 15px; font-weight: 400;
    color: var(--ink-grey);
  }
</style>
</head>
<body>
<main class="canvas">

  <section class="card card--front" aria-label="Business card front">
    <div class="card__rotated">
      <div class="blue-panel"></div>
      <div class="skyline" role="img" aria-label="Blue silhouette of the City of London skyline with the Pinecone, a tower, a bridge and an observation wheel"></div>

      <div class="brand">
        <span class="brand__mark"></span>
        <span class="brand__name">The Harrowfield Clinic</span>
      </div>
      <div class="brand__tagline">Private General Practice</div>

      <div class="contact">
        <div class="contact__name">ALEX MORROW</div>
        <div class="contact__role">CEO/FOUNDER</div>
        <div class="contact__address">
          FitVanta<br>
          19 Bramblecote Lane<br>
          London, EC2Z 4QJ
        </div>
        <div class="contact__line">
          <svg class="contact__icon" viewBox="0 0 12 12" aria-hidden="true"><path d="M2.5 1h2l1 2.5-1.3 1a6 6 0 0 0 3.3 3.3l1-1.3L11 7.5v2a1.2 1.2 0 0 1-1.3 1.2A9 9 0 0 1 1.3 2.3 1.2 1.2 0 0 1 2.5 1z" fill="#fff"/></svg>
          <span>020 7946 0381</span>
        </div>
        <div class="contact__line">
          <svg class="contact__icon" viewBox="0 0 12 12" aria-hidden="true"><rect x="0.5" y="2" width="11" height="8" fill="#fff"/><path d="M0.5 2 6 6.5 11.5 2" fill="none" stroke="#4aa9d4" stroke-width="1"/></svg>
          <span>bookings@harrowfieldclinic.example</span>
        </div>
        <div class="contact__line">
          <svg class="contact__icon" viewBox="0 0 12 12" aria-hidden="true"><circle cx="6" cy="6" r="5.5" fill="#fff"/><path d="M0.5 6h11M6 0.5c-2.5 3-2.5 8 0 11M6 0.5c2.5 3 2.5 8 0 11" fill="none" stroke="#4aa9d4" stroke-width="0.9"/></svg>
          <span>www.harrowfieldclinic.example</span>
        </div>
      </div>
    </div>
  </section>

  <section class="card card--back" aria-label="Business card back">
    <div class="back-brand">
      <span class="brand__mark"></span>
      <span class="brand__name">The Harrowfield Clinic</span>
    </div>
    <p class="opening-hours">Open: Mon-Fri (early &amp; late appointments)</p>
  </section>

</main>
</body>
</html>
```